Business card design needed

We would like a new design for our window furnishings & home decor business. We supply & install blinds, curtains, shutters etc. We are about to incorporate home decor products like cushoins & throws...
We'd like to use moderns browns & green tones. Casual but elegant style. Maybe textured/patterned look design. Design should communicate quality and great value with latest designs.

website & FB page & email is still to be advised so pls provide space.

Industry/Entity Type

Business

Contact Information for Business Card

Marlowe Haven
Window Furnishings & Home Decor
Genevieve - Interior Stylist
Call us now for a free measure & quote - 63124089
0412 906 358
0418 273 564

```html
<!DOCTYPE html>
<html lang="en">
<head>
<meta charset="utf-8">
<title>Marlowe Haven – Business Card</title>
<link href="https://fonts.googleapis.com/css2?family=Almendra&family=Cormorant+Garamond:ital,wght@1,500&family=PT+Sans&display=swap" rel="stylesheet">
<style>
  :root {
    --page: #ffffff;
    --card-black: #0d0b0a;
    --card-brown: #3a1a0c;
    --gold: #b8891f;
    --gold-light: #f3d36a;
    --gold-deep: #8a4d10;
    --band-edge: #5a2a0c;
    --ink-brown: #5b260c;
    --white: #ffffff;
  }
  * { margin: 0; padding: 0; box-sizing: border-box; }
  html, body { width: 1200px; height: 398px; overflow: hidden; background: var(--page); }
  .canvas { position: relative; width: 1200px; height: 398px; }

  .card {
    position: absolute;
    width: 476px; height: 267px;
    border-radius: 14px;
    overflow: hidden;
  }
  .card--front {
    left: 125px; top: 63px;
    background: radial-gradient(ellipse 70% 90% at 88% 55%, var(--card-brown) 0%, var(--card-black) 75%);
  }
  .card--back {
    left: 700px; top: 65px;
    background: radial-gradient(ellipse 60% 80% at 10% 95%, var(--card-brown) 0%, var(--card-black) 70%);
  }

  .band { position: absolute; inset: 0; }
  .ornament {
    position: absolute;
    border-radius: 40%;
    background: radial-gradient(ellipse at center, rgba(184,137,31,0.45) 0%, rgba(184,137,31,0.12) 55%, rgba(184,137,31,0) 75%);
  }
  .ornament--front-left { left: 10px; top: 10px; width: 90px; height: 200px; }
  .ornament--front-right { left: 286px; top: 30px; width: 90px; height: 230px; }
  .ornament--back { left: 14px; top: 86px; width: 240px; height: 80px; }

  .front-name {
    position: absolute;
    left: 78px; width: 216px;
    text-align: center;
    font-family: "Almendra", serif;
    font-size: 47px;
    line-height: 1;
    color: var(--ink-brown);
  }
  .front-name--first { top: 58px; }
  .front-name--second { top: 141px; }

  .role {
    position: absolute;
    left: 78px; width: 216px; top: 229px;
    text-align: center;
    font-family: "Cormorant Garamond", serif;
    font-style: italic; font-weight: 500;
    font-size: 15px;
    letter-spacing: 3px;
    color: #fff3c8;
  }

  .back-name {
    position: absolute;
    left: 16px; top: 14px;
    font-family: "Almendra", serif;
    font-size: 58px;
    line-height: 1;
    color: var(--gold);
  }
  .tagline {
    position: absolute;
    right: 16px; top: 118px;
    text-align: right;
    font-family: "Cormorant Garamond", serif;
    font-style: italic; font-weight: 500;
    font-size: 23px;
    line-height: 37px;
    letter-spacing: 0.5px;
    color: var(--white);
  }
  .call {
    position: absolute;
    left: 111px; top: 201px;
    font-family: "PT Sans", sans-serif;
    font-size: 17.5px;
    color: var(--gold);
  }
  .phones {
    position: absolute;
    left: 111px; top: 226px;
    font-family: "PT Sans", sans-serif;
    font-size: 19px;
    color: var(--gold);
    white-space: nowrap;
  }
  .phones .sep {
    display: inline-block;
    width: 4px; height: 4px;
    margin: 0 6px 4px;
    border-radius: 50%;
    background: var(--gold);
    vertical-align: middle;
  }
</style>
</head>
<body>
<main class="canvas">

  <section class="card card--front" aria-label="Business card front">
    <svg class="band" viewBox="0 0 476 267" aria-hidden="true">
      <defs>
        <linearGradient id="band-gold" x1="0" y1="0" x2="0" y2="1">
          <stop offset="0" stop-color="#8a4d10"/>
          <stop offset="0.3" stop-color="#c7891f"/>
          <stop offset="0.65" stop-color="#e8b935"/>
          <stop offset="1" stop-color="#f4d56b"/>
        </linearGradient>
      </defs>
      <path d="M80 0 Q100 133 74 267 L295 267 Q272 133 293 0 Z" fill="url(#band-gold)" stroke="var(--band-edge)" stroke-width="6"/>
      <path d="M72 0 Q92 133 66 267" fill="none" stroke="#b07a22" stroke-width="1.5"/>
      <path d="M301 0 Q280 133 303 267" fill="none" stroke="#b07a22" stroke-width="1.5"/>
    </svg>
    <div class="ornament ornament--front-left" role="img" aria-label="Gold scroll flourish ornament"></div>
    <div class="ornament ornament--front-right" role="img" aria-label="Gold scroll flourish ornament"></div>
    <p class="front-name front-name--first">Marlowe</p>
    <p class="front-name front-name--second">Haven</p>
    <p class="role">Interior Stylist</p>
  </section>

  <section class="card card--back" aria-label="Business card back">
    <div class="ornament ornament--back" role="img" aria-label="Gold scroll flourish ornament"></div>
    <h1 class="back-name">Marlowe Haven</h1>
    <p class="tagline">Window Furnishings<br>&amp; Home Decor Genevieve</p>
    <p class="call">Call us now for a free measure &amp; quote</p>
    <p class="phones">63124089<span class="sep"></span>0412 906 358<span class="sep"></span>0418 273 564</p>
  </section>

</main>
</body>
</html>
```